Presentation Flyer for Married Couple at night separate business owners by day

I would like a flyer to use to advertise free presentations put on by husband and I. I (Renata Volkhaven) am an estate planning attorney that works for PWR Law. My husband (Dan Volkhaven) is a financial planner that works for Quelmora Financial Planning. Would love it to be funny but serious. At night we are a married couple of 4 children, by day we individually work with people helping them protect their assets and their families.
Goal is for this to be used for multiple events.
Things to include: Food will be provided, Raffle for $500 off an Estate Plan Package
Topics to be covered in Seminar:
Estate & Financial Planning Essentials

Protect Your Future
Build a strong financial foundation with emergency funds, retirement planning, and smart investment strategies that match your goals.

Secure Your Legacy
Learn about wills, trusts, and powers of attorney - the essential documents everyone needs to protect their family's future.

Guard Your Assets
Understand the right insurance coverage to protect yourself and your loved ones, from life insurance to long-term care options.

Transfer Wealth Wisely
Discover tax-efficient strategies for passing assets to the next generation and making the most of your charitable giving.

```html
<!DOCTYPE html>
<html lang="en">
<head>
<meta charset="utf-8">
<title>Estate &amp; Financial Planning Essentials</title>
<link rel="stylesheet" href="https://fonts.googleapis.com/css2?family=Montserrat:wght@400;500;600;700;800;900&display=swap">
<style>
  :root {
    --stage: #4a4a4a;
    --paper: #f3f4f5;
    --paper-deep: #e4e6e8;
    --teal: #1d6f73;
    --teal-light: #26a39c;
    --blue: #0f5fa8;
    --blue-bright: #2b8fd6;
    --navy: #0d2a4a;
    --ink: #1c2330;
    --white: #ffffff;
  }
  * { box-sizing: border-box; margin: 0; padding: 0; }
  html, body { width: 1200px; height: 2408px; overflow: hidden; }
  body { background: var(--stage); font-family: "Montserrat", sans-serif; position: relative; }

  .flyer {
    position: absolute; left: 62.4px; top: 440.8px;
    width: 896px; height: 1272px;
    transform: scale(1.2); transform-origin: 0 0;
    background: linear-gradient(180deg, var(--paper) 0%, #ffffff 55%, var(--paper-deep) 100%);
    overflow: hidden;
    box-shadow: 0 20px 40px rgba(0,0,0,.35);
  }
  .layer { position: absolute; left: 0; top: 0; width: 896px; height: 1272px; }

  .backdrop {
    position: absolute; left: 0; top: 0; width: 896px; height: 240px;
    background: linear-gradient(90deg, #e9ebed, #dcdfe2 60%, #e6e8ea);
  }

  .brand-law {
    position: absolute; left: 75px; top: 80px; width: 310px;
    display: flex; align-items: center; gap: 12px;
    font-weight: 800; font-size: 46px; color: var(--navy); letter-spacing: 1px;
  }
  .brand-law .mark { width: 22px; height: 22px; background: var(--blue); }

  .portrait-frame { position: absolute; left: 428px; top: 0; width: 168px; height: 225px; background: var(--teal); }
  .portrait {
    position: absolute; left: 436px; top: 58px; width: 150px; height: 149px;
    background: linear-gradient(160deg, #a0674a 0%, #6d4a3c 40%, #2b2f3a 100%);
  }

  .brand-fin {
    position: absolute; left: 640px; top: 110px; width: 205px; text-align: center;
    font-weight: 700; color: var(--navy);
  }
  .brand-fin .name { font-size: 30px; letter-spacing: 1px; }
  .brand-fin .sub { font-size: 12px; letter-spacing: 2px; margin-top: 4px; color: var(--navy); }

  .hero-photo { position: absolute; }

  .title {
    position: absolute; left: 57px; top: 340px;
    font-weight: 900; font-size: 66px; line-height: 66px; letter-spacing: -1px; color: var(--white);
  }
  .title .teal { color: var(--teal-light); }
  .title .amp { color: var(--teal-light); font-weight: 500; }
  .title .blue { color: var(--blue-bright); font-weight: 500; }

  .ribbon-text { position: absolute; left: 185px; top: 575px; color: var(--white); }
  .ribbon-text .lead { font-weight: 700; font-size: 35px; line-height: 42px; }
  .ribbon-text .raffle { font-weight: 500; font-size: 25px; line-height: 34px; }
  .ribbon-text .amount { font-weight: 800; font-size: 33px; }

  .topics { position: absolute; left: 57px; top: 742px; width: 770px; list-style: none; }
  .topic {
    display: flex; gap: 30px; height: 110px; padding-top: 6px;
    border-bottom: 1.5px solid var(--navy);
  }
  .topic:first-child { height: 100px; padding-top: 6px; }
  .topic + .topic { padding-top: 10px; }
  .topic:last-child { border-bottom: none; }
  .topic-icon { flex: 0 0 62px; width: 62px; height: 62px; background: var(--blue); display: flex; align-items: center; justify-content: center; }
  .topic-title { font-size: 26px; font-weight: 500; color: var(--blue); line-height: 30px; }
  .topic-title strong { font-weight: 800; }
  .topic-body { font-size: 17px; line-height: 23px; color: var(--ink); margin-top: 4px; }

  .presenters {
    position: absolute; left: 0; top: 1185px; width: 830px; text-align: center;
    font-size: 21px; color: var(--white); font-weight: 400;
  }
</style>
</head>
<body>
<main class="flyer">
  <div class="backdrop" role="img" aria-label="Faded photograph of modern office buildings"></div>

  <svg class="layer" viewBox="0 0 896 1272" aria-hidden="true">
    <g fill="var(--blue)">
      <rect x="4" y="0" width="4" height="130"/><rect x="13" y="0" width="4" height="130"/>
      <rect x="22" y="0" width="4" height="130"/><rect x="31" y="0" width="4" height="130"/>
    </g>
    <g fill="var(--teal)">
      <rect x="856" y="555" width="4" height="717"/><rect x="866" y="555" width="4" height="717"/>
      <rect x="876" y="555" width="4" height="717"/><rect x="886" y="555" width="4" height="717"/>
    </g>
    <polygon points="310,225 380,200 450,225" fill="var(--blue)"/>
    <polygon points="0,225 690,225 860,430 830,430 680,252 0,252" fill="var(--teal)"/>
    <polygon points="790,230 880,230 855,255 896,300 896,380 830,290 808,312" fill="var(--teal-light)"/>
  </svg>

  <svg class="layer hero-photo" viewBox="0 0 896 1272" role="img" aria-label="Photograph of business people shaking hands over financial documents">
    <defs>
      <linearGradient id="heroShade" x1="0" y1="0" x2="1" y2="0">
        <stop offset="0" stop-color="#5b5550"/>
        <stop offset=".45" stop-color="#1c1d22"/>
        <stop offset="1" stop-color="#101318"/>
      </linearGradient>
    </defs>
    <polygon points="0,270 690,270 858,430 780,560 0,560" fill="url(#heroShade)"/>
  </svg>

  <svg class="layer" viewBox="0 0 896 1272" aria-hidden="true">
    <polygon points="0,560 870,560 780,676 135,676 110,695 20,676 0,640" fill="var(--blue)"/>
    <polygon points="0,620 70,676 20,676 0,660" fill="#3a7fc4"/>
    <polygon points="0,1140 0,1272 140,1272" fill="var(--blue)"/>
    <g stroke="var(--blue)" stroke-width="3">
      <line x1="0" y1="1165" x2="130" y2="1272"/>
      <line x1="0" y1="1185" x2="105" y2="1272"/>
    </g>
    <polygon points="50,1183 740,1183 758,1235 50,1235" fill="var(--teal)"/>
  </svg>

  <div class="brand-law"><span class="mark"></span>PWR Law</div>

  <div class="portrait-frame"></div>
  <div class="portrait" role="img" aria-label="Portrait photograph of the two presenters"></div>

  <div class="brand-fin">
    <div class="name">QUELMORA</div>
    <div class="sub">FINANCIAL PLANNING</div>
  </div>

  <h1 class="title">
    <span class="teal">ESTATE</span> <span class="amp">&amp;</span> FINANCIAL<br>
    PLANNING <span class="blue">ESSENTIALS</span>
  </h1>

  <div class="ribbon-text">
    <p class="lead">Food will be provided,</p>
    <p class="raffle">Raffle for <span class="amount">$500</span> of an Estate Plan Package</p>
  </div>

  <ul class="topics">
    <li class="topic">
      <div class="topic-icon">
        <svg width="40" height="40" viewBox="0 0 40 40" fill="none" stroke="#fff" stroke-width="2">
          <circle cx="22" cy="12" r="7"/><path d="M15 12h14M22 5v14"/>
          <path d="M4 26h8l8 4h10l6-5"/><path d="M4 24v10"/>
        </svg>
      </div>
      <div>
        <h2 class="topic-title">Protect <strong>Your Future</strong></h2>
        <p class="topic-body">Build a strong financial foundation with emergency funds, retirement planning, and smart investment strategies that match your goals.</p>
      </div>
    </li>
    <li class="topic">
      <div class="topic-icon">
        <svg width="40" height="40" viewBox="0 0 40 40" fill="none" stroke="#fff" stroke-width="2">
          <rect x="8" y="5" width="20" height="28"/><path d="M12 13h12M12 18h12M12 23h8"/>
          <rect x="24" y="26" width="10" height="8" fill="#fff"/><path d="M26 26v-3a3 3 0 0 1 6 0v3"/>
        </svg>
      </div>
      <div>
        <h2 class="topic-title">Secure <strong>Your Legacy</strong></h2>
        <p class="topic-body">Learn about wills, trusts, and powers of attorney - the essential documents everyone needs to protect their family's future.</p>
      </div>
    </li>
    <li class="topic">
      <div class="topic-icon">
        <svg width="40" height="40" viewBox="0 0 40 40" fill="none" stroke="#fff" stroke-width="2">
          <path d="M20 4l13 5v10c0 9-6 14-13 17C13 33 7 28 7 19V9z"/>
          <circle cx="20" cy="19" r="7"/>
          <path d="M22.5 16c-1-1-5-1-5 1s5 1 5 3.5-4 2-5 1M20 14v10"/>
        </svg>
      </div>
      <div>
        <h2 class="topic-title">Guard <strong>Your Assets</strong></h2>
        <p class="topic-body">Understand the right insurance coverage to protect yourself and your loved ones, from life insurance to long-term care options.</p>
      </div>
    </li>
    <li class="topic">
      <div class="topic-icon">
        <svg width="40" height="40" viewBox="0 0 40 40" fill="none" stroke="#fff" stroke-width="2">
          <path d="M12 35v-7c-4-3-6-7-5-12 1-6 6-10 13-10 7 0 12 5 12 11 0 2 2 5 3 7h-3v5h-6v6"/>
          <path d="M16 14h8l-3-3M24 20h-8l3 3"/>
        </svg>
      </div>
      <div>
        <h2 class="topic-title">Transfer <strong>Wealth Wisely</strong></h2>
        <p class="topic-body">Discover tax-efficient strategies for passing assets to the next generation and making the most of your charitable giving.</p>
      </div>
    </li>
  </ul>

  <p class="presenters">Renata Volkhaven , Dan Volkhaven</p>
</main>
</body>
</html>
```